Healthy Supplement featuring Moringa products

Need 3 business card options for our reps to order from Cardloom. Our reps will be ordering from Cardloom once we upload them. Attached is our current designs to show what info needs to be on the cards. Our website is www.tkvitality.com
The business cards will be a template for our reps to order from. Most of our reps are Asian & Hispanic. Please look at our website so you can see who we are to get the look and feel what we need.
Target Market(s)
Adults 30 on up. Health oriented people.
Industry/Entity Type
Health And Wellness
Contact Information for Business Card
Name
Title
Phone
Logo
www.tkvitality.com/my/username
Font styles to use
Requirements
Must have
- Please match our website look and colors. A moringa leaf is nice, but am open to something different.
Nice to have
- Healthy looking and warm, not super cold or too modern.
Should not have
- No harsh colors please.

```html
<!DOCTYPE html>
<html lang="en">
<head>
<meta charset="utf-8">
<title>TK Vitality Business Card</title>
<link href="https://fonts.googleapis.com/css2?family=Cinzel:wght@400;600&family=Roboto:wght@400;700&display=swap" rel="stylesheet">
<style>
  :root{
    --stage:#2b2b2b;
    --orange:#f7931e;
    --green:#6aa80f;
    --green-light:#8cc63f;
    --white:#ffffff;
  }
  html,body{margin:0;padding:0;overflow:hidden;}
  body{width:1200px;height:768px;background:var(--stage);position:relative;font-family:"Roboto",sans-serif;}
  .card{position:absolute;top:230px;width:540px;height:308px;border-radius:18px;overflow:hidden;}
  .card-back{left:40px;background:var(--orange);}
  .card-front{left:620px;background:var(--white);}
  .back-brand{position:absolute;left:0;right:0;top:112px;text-align:center;color:var(--white);
    font-family:"Cinzel",serif;font-weight:600;font-size:44px;letter-spacing:2px;}
  .back-brand .dot{display:inline-block;width:16px;height:16px;border-radius:50%;background:var(--white);margin-right:14px;vertical-align:middle;}
  .back-url{position:absolute;left:0;right:0;bottom:40px;text-align:center;color:var(--white);
    font-family:"Roboto",sans-serif;font-size:12px;letter-spacing:5px;}
  .front-shape{position:absolute;inset:0;}
  .front-brand{position:absolute;left:30px;width:250px;top:104px;text-align:center;color:var(--green-light);
    font-family:"Cinzel",serif;font-weight:600;font-size:34px;line-height:1.15;letter-spacing:2px;}
  .front-brand .dot{display:block;width:30px;height:30px;border-radius:50%;background:var(--green-light);margin:0 auto 10px;}
  .contact{position:absolute;left:330px;top:112px;color:var(--white);}
  .contact-name{font-family:"Cinzel",serif;font-size:20px;letter-spacing:1px;margin:0;}
  .contact-title{font-family:"Roboto",sans-serif;font-weight:700;font-size:14px;margin:2px 0 12px;}
  .contact-line{display:flex;align-items:center;gap:8px;font-size:13px;margin:4px 0;}
  .contact-line svg{width:12px;height:12px;flex:none;}
</style>
</head>
<body>
  <section class="card card-back">
    <div class="back-brand"><span class="dot"></span>TK Vitality</div>
    <div class="back-url">www.tkvitality.com</div>
  </section>

  <section class="card card-front">
    <svg class="front-shape" viewBox="0 0 540 308" width="540" height="308">
      <path d="M318 0 C308 120 238 236 132 308 L146 308 C248 236 318 120 330 0 Z" fill="var(--orange)"/>
      <path d="M330 0 C318 120 248 236 146 308 L540 308 L540 0 Z" fill="var(--green)"/>
    </svg>
    <div class="front-brand"><span class="dot"></span>TK Vitality</div>
    <div class="contact">
      <p class="contact-name">DANIEL REYES</p>
      <p class="contact-title">President</p>
      <div class="contact-line">
        <svg viewBox="0 0 12 12"><path d="M2.5 1 L4.5 1 L5.2 3.5 L4 4.6 C4.7 6 6 7.3 7.4 8 L8.5 6.8 L11 7.5 L11 9.5 C11 10.3 10.3 11 9.5 11 C5 11 1 7 1 2.5 C1 1.7 1.7 1 2.5 1Z" fill="var(--white)"/></svg>
        <span>+1(555)214-0387</span>
      </div>
      <div class="contact-line">
        <svg viewBox="0 0 12 12"><rect x="0.5" y="2" width="11" height="8" fill="var(--white)"/><path d="M0.5 2 L6 6.5 L11.5 2" fill="none" stroke="var(--green)" stroke-width="1"/></svg>
        <span>info@tkvitality.com</span>
      </div>
      <div class="contact-line">
        <svg viewBox="0 0 12 12"><circle cx="6" cy="6" r="5.5" fill="var(--white)"/><path d="M0.5 6 H11.5 M6 0.5 C3.5 3 3.5 9 6 11.5 M6 0.5 C8.5 3 8.5 9 6 11.5" fill="none" stroke="var(--green)" stroke-width="0.8"/></svg>
        <span>www.tkvitality.com</span>
      </div>
    </div>
  </section>
</body>
</html>
```